quality electrical business needs a logo design

we need a logo design for our new company starting up. I'm a sole trader electrician. I want to make the VES prominent in Vellar Electrical Services. Information I would want on the business card would be;
Business Name: Vellar Electrical Services
What I do: Domestic/Commercial/Industrial Installation & Maintenance
Email Address: Brenton.vellar@qorvamail.net.au
Contact no: Brenton 0438261574
Electrical License no: EC47391

Open to different Colours but would like to see some with Navy blue. I want to promote professionalism and have a modern feel about it.

```html
<!DOCTYPE html>
<html lang="en">
<head>
<meta charset="utf-8">
<title>Vellar Electrical Services – Business Card</title>
<link rel="stylesheet" href="https://fonts.googleapis.com/css2?family=Open+Sans:wght@400;600;700&display=swap">
<style>
  :root {
    --navy: #1a1464;
    --blue: #1f7ac4;
    --card: #ffffff;
    --backdrop: #9a9a9a;
    --backdrop-light: #bdbdbd;
  }
  * { margin: 0; padding: 0; box-sizing: border-box; }
  html, body {
    width: 1200px;
    height: 900px;
    overflow: hidden;
  }
  body {
    background: radial-gradient(ellipse at 30% 35%, var(--backdrop-light), var(--backdrop) 70%);
    font-family: "Open Sans", sans-serif;
    position: relative;
  }
  .business-card {
    position: absolute;
    left: 160px;
    top: 230px;
    width: 880px;
    height: 440px;
    background: var(--card);
    box-shadow: 0 14px 40px rgba(0,0,0,0.25);
    overflow: hidden;
  }
  .licence-number {
    position: absolute;
    top: 22px;
    right: 32px;
    font-size: 15px;
    color: var(--navy);
    letter-spacing: 0.5px;
  }
  .brand {
    position: absolute;
    left: 40px;
    top: 78px;
    display: flex;
    align-items: center;
    gap: 16px;
  }
  .brand-square {
    width: 34px;
    height: 34px;
    background: var(--navy);
  }
  .brand-name {
    font-size: 38px;
    font-weight: 600;
    color: var(--navy);
    letter-spacing: 0.3px;
  }
  .rule {
    position: absolute;
    height: 2px;
    background: var(--navy);
  }
  .rule-left { left: 0; top: 228px; width: 470px; }
  .rule-right { left: 720px; top: 228px; right: 32px; }
  .contact-name {
    position: absolute;
    left: 494px;
    top: 209px;
    font-size: 28px;
    font-weight: 700;
    color: var(--blue);
  }
  .contact-details {
    position: absolute;
    left: 496px;
    top: 268px;
    list-style: none;
    font-size: 16px;
    color: var(--navy);
    line-height: 30px;
  }
  .contact-details b {
    font-weight: 700;
    display: inline-block;
    width: 24px;
  }
  .service-list {
    position: absolute;
    left: 40px;
    top: 262px;
    list-style: none;
    font-size: 19px;
    color: var(--navy);
    line-height: 32px;
  }
  .service-list li::before {
    content: "";
    display: inline-block;
    width: 7px;
    height: 7px;
    border-radius: 50%;
    background: var(--navy);
    margin-right: 16px;
    vertical-align: middle;
  }
  .footer-band {
    position: absolute;
    left: 0;
    right: 0;
    bottom: 0;
    height: 40px;
    background: var(--navy);
  }
</style>
</head>
<body>
  <section class="business-card">
    <p class="licence-number">EC47391</p>

    <div class="brand">
      <span class="brand-square"></span>
      <span class="brand-name">Vellar Electrical Services</span>
    </div>

    <div class="rule rule-left"></div>
    <h1 class="contact-name">Brenton Vellar</h1>
    <div class="rule rule-right"></div>

    <ul class="contact-details">
      <li><b>P:</b>0438 261 574</li>
      <li><b>E:</b>Brenton.vellar@qorvamail.net.au</li>
    </ul>

    <ul class="service-list">
      <li>Domestic</li>
      <li>Commercial</li>
      <li>Industrial Installation &amp; Maintenance</li>
    </ul>

    <div class="footer-band"></div>
  </section>
</body>
</html>
```